Consulting company requires a logo and business card design

I require a logo/business card design for a new company based in Sexsmith Alberta called TanRidge Field Advisory Ltd. I plan to provide the following services: Construction management/inspection for the oil and gas industry, as well as general consulting for Asset Management, fleet management, etc. Have attached a copy of resume for use as guide for

Target Market(s)

Businesses within the oil and gas production, construction and shipping industry

Industry/Entity Type

Oil And Gas

Contact Information for Business Card

Believe should highlight, services offered, safety, quality,

Logo Text

TanRidge Field Advisory (TRFA) ?

Font styles to use
Script

Requirements
Must have
• Open to all options

```html
<!DOCTYPE html>
<html lang="en">
<head>
<meta charset="utf-8">
<title>TanRidge Field Advisory Ltd. — Logo and Business Card</title>
<link rel="stylesheet" href="https://fonts.googleapis.com/css2?family=Cinzel:wght@600&family=Open+Sans:wght@400&display=swap">
<style>
  :root {
    --brand-blue: #1f4a92;
    --band-blue-dark: #1b2f78;
    --band-blue-light: #1d63a8;
    --band-grey-dark: #2e2e2e;
    --band-grey-light: #5a5a5a;
    --ink: #2b2b2b;
    --rule: #cfcfcf;
    --paper: #ffffff;
    --stage: #e4e4e6;
  }
  * { margin: 0; padding: 0; box-sizing: border-box; }
  html, body { width: 994px; height: 1200px; overflow: hidden; }
  body { position: relative; background: var(--paper); font-family: "Open Sans", Arial, sans-serif; color: var(--ink); }

  .brand-sheet { position: absolute; left: 0; top: 0; width: 994px; height: 370px; background: var(--paper); }
  .card-sheet { position: absolute; left: 0; top: 370px; width: 994px; height: 830px; background: var(--stage); }

  .wordmark { position: absolute; display: flex; align-items: center; }
  .wordmark-dot { flex: none; border-radius: 50%; background: var(--brand-blue); }
  .wordmark-name {
    font-family: "Cinzel", "Times New Roman", serif;
    font-weight: 600;
    color: var(--brand-blue);
    line-height: 1.15;
    letter-spacing: 0.02em;
  }

  .wordmark--hero { left: 250px; top: 130px; gap: 30px; }
  .wordmark--hero .wordmark-dot { width: 110px; height: 110px; }
  .wordmark--hero .wordmark-name { font-size: 38px; }

  .business-card { position: absolute; left: 219px; width: 552px; height: 329px; background: var(--paper); overflow: hidden; }
  .business-card--front { top: 431px; }
  .business-card--back { top: 811px; }

  .wordmark--card { left: 262px; top: 48px; gap: 14px; }
  .wordmark--card .wordmark-dot { width: 46px; height: 46px; }
  .wordmark--card .wordmark-name { font-size: 19px; }

  .wordmark--back { left: 95px; top: 116px; gap: 22px; }
  .wordmark--back .wordmark-dot { width: 84px; height: 84px; }
  .wordmark--back .wordmark-name { font-size: 27px; }

  .holder { position: absolute; left: 28px; top: 164px; }
  .holder-name { font-family: "Cinzel", "Times New Roman", serif; font-weight: 600; font-size: 18px; color: var(--brand-blue); letter-spacing: 0.01em; }
  .holder-role { font-size: 13px; margin-top: 1px; }

  .divider { position: absolute; left: 28px; top: 220px; width: 374px; height: 1px; background: var(--rule); }

  .address { position: absolute; left: 28px; top: 243px; font-size: 13.5px; line-height: 18px; font-style: normal; }

  .contact-list { position: absolute; right: 28px; top: 212px; list-style: none; text-align: right; font-size: 13.5px; line-height: 20.5px; }
  .contact-list li { display: flex; justify-content: flex-end; align-items: center; gap: 6px; }
  .contact-list svg { width: 12px; height: 12px; fill: var(--brand-blue); flex: none; }

  .card-band { position: absolute; left: 0; bottom: 0; width: 552px; height: 22px; }
</style>
</head>
<body>
  <section class="brand-sheet">
    <div class="wordmark wordmark--hero">
      <span class="wordmark-dot"></span>
      <span class="wordmark-name">TanRidge Field<br>Advisory Ltd.</span>
    </div>
  </section>

  <section class="card-sheet"></section>

  <article class="business-card business-card--front">
    <div class="wordmark wordmark--card">
      <span class="wordmark-dot"></span>
      <span class="wordmark-name">TanRidge Field<br>Advisory Ltd.</span>
    </div>

    <div class="holder">
      <h1 class="holder-name">DANIEL MORROW</h1>
      <p class="holder-role">Managing Director</p>
    </div>

    <div class="divider"></div>

    <address class="address">
      Unit 4, 9814 100 Avenue<br>
      Sexsmith, Alberta
    </address>

    <ul class="contact-list">
      <li>+ 000 000 0000
        <svg viewBox="0 0 12 12" aria-hidden="true"><path d="M3.5 0h5a1 1 0 0 1 1 1v10a1 1 0 0 1-1 1h-5a1 1 0 0 1-1-1V1a1 1 0 0 1 1-1zm.5 1.5v6h4v-6zm2 7.5a.9.9 0 1 0 0 1.8.9.9 0 0 0 0-1.8z"/></svg>
      </li>
      <li>+ 000 000 0000
        <svg viewBox="0 0 12 12" aria-hidden="true"><path d="M1 4c0-1.5 2.2-2.5 5-2.5S11 2.5 11 4v1H8.5V3.8h-5V5H1zm2.2 2h5.6l1.7 4.5H1.5z"/></svg>
      </li>
      <li>info@tanridgefa.com
        <svg viewBox="0 0 12 12" aria-hidden="true"><path d="M0 2.5h12v7H0zm1 .8 5 3.6 5-3.6v-.1H1z"/></svg>
      </li>
      <li>www.tanridgefa.com
        <svg viewBox="0 0 12 12" aria-hidden="true"><path d="M6 0a6 6 0 1 0 0 12A6 6 0 0 0 6 0zm0 1.2c.8 0 1.6 1.9 1.7 4.2H4.3C4.4 3.1 5.2 1.2 6 1.2zM1.2 6.6h2.1c.1 1.6.4 3 .9 3.9A4.8 4.8 0 0 1 1.2 6.6zm0-1.2a4.8 4.8 0 0 1 3-3.9c-.5.9-.8 2.3-.9 3.9zm4.8 5.4c-.8 0-1.6-1.9-1.7-4.2h3.4c-.1 2.3-.9 4.2-1.7 4.2zm1.8-.3c.5-.9.8-2.3.9-3.9h2.1a4.8 4.8 0 0 1-3 3.9zm.9-5.1c-.1-1.6-.4-3-.9-3.9a4.8 4.8 0 0 1 3 3.9z"/></svg>
      </li>
    </ul>

    <svg class="card-band" viewBox="0 0 552 22" preserveAspectRatio="none" aria-hidden="true">
      <defs>
        <linearGradient id="band-blue" x1="0" x2="1">
          <stop offset="0" stop-color="var(--band-blue-dark)"/>
          <stop offset="1" stop-color="var(--band-blue-light)"/>
        </linearGradient>
        <linearGradient id="band-grey" x1="0" x2="1">
          <stop offset="0" stop-color="var(--band-grey-light)"/>
          <stop offset="1" stop-color="var(--band-grey-dark)"/>
        </linearGradient>
      </defs>
      <polygon points="0,9 280,9 265,22 0,22" fill="url(#band-blue)"/>
      <polygon points="292,0 552,0 552,22 270,22" fill="url(#band-grey)"/>
    </svg>
  </article>

  <article class="business-card business-card--back">
    <div class="wordmark wordmark--back">
      <span class="wordmark-dot"></span>
      <span class="wordmark-name">TanRidge Field<br>Advisory Ltd.</span>
    </div>
  </article>
</body>
</html>
```